Büroausstattung Steuerberater
Alles prima. Frau Wendtke arbeitet äußerst professionell und wird von uns auch zukünftig für anstehende Arbeiten beauftragt!
Zielgruppe
Typisch Steuerberater: Vom jungen Existenzgründer bis zum Geschäftsführer eines großen Unternehmens.
Mit anderen Worten: Nicht verspielt, aber auch nicht zu bieder.
Aufgabenstellung
Wir benötigen:
-Allg. Briefpapier
-Rechnungsvorlage (mit einfacher Excel-Addition)
-Faxvorlage
-Visitenkarten
-Memo Block (DIN A4 - kariert)
Wichtig:
Wir benötigen nicht nur einen Designvorschlag, sondern fertige Word bzw. Excel Dokumente, mit denen wir direkt arbeiten bzw. diese ausdrucken können!
Da wir bereits ein Logo haben, ist die Kreierung eines Logos nicht erforderlich.

```html
<!DOCTYPE html>
<html lang="de">
<head>
<meta charset="utf-8">
<title>Büroausstattung Steuerberater – Briefpapier und Visitenkarte</title>
<link rel="stylesheet" href="https://fonts.googleapis.com/css2?family=Arimo:wght@400;700&display=swap">
<style>
  :root {
    --brand-blue: #1f3a8f;
    --brand-deep: #1a2f7a;
    --ink: #1a1a1a;
    --paper: #ffffff;
    --stage: #e4e5e7;
    --fold: #6f86c6;
  }
  * { box-sizing: border-box; margin: 0; padding: 0; }
  html, body { width: 1200px; height: 861px; overflow: hidden; }
  body {
    background: var(--stage);
    font-family: "Arimo", Arial, sans-serif;
    color: var(--ink);
    position: relative;
  }

  /* ---------- Letterhead ---------- */
  .letterhead {
    position: absolute; left: 147px; top: 23px;
    width: 568px; height: 801px;
    background: var(--paper);
  }
  .brand {
    position: absolute; display: flex; align-items: center; gap: 8px;
    color: var(--brand-blue); font-weight: 700; white-space: nowrap;
  }
  .letterhead .brand { right: 34px; top: 50px; font-size: 28px; }
  .brand-square { display: block; width: 14px; height: 14px; background: var(--brand-blue); }

  .return-line {
    position: absolute; left: 53px; top: 118px; width: 250px;
    font-size: 6.5px; color: var(--brand-blue);
    border-bottom: 0.8px solid var(--brand-blue); padding-bottom: 2px;
  }
  .recipient {
    position: absolute; left: 64px; top: 156px;
    font-size: 11.5px; line-height: 14.5px;
  }
  .references {
    position: absolute; left: 339px; top: 158px;
    font-size: 9.5px; line-height: 12.5px; font-weight: 700; color: var(--brand-blue);
  }
  .references .date { margin-top: 23px; }
  .fold-mark {
    position: absolute; left: 0; width: 12px; height: 1px; background: var(--fold);
  }
  .letter-body {
    position: absolute; left: 64px; top: 292px; width: 462px;
    font-size: 11.3px; line-height: 15.3px;
  }
  .letter-body p { margin-bottom: 15px; }
  .signature {
    position: absolute; left: 64px; top: 612px; width: 90px; height: 18px;
    background: linear-gradient(90deg, #3a3a3a 0%, #8a8a8a 100%); opacity: .35; border-radius: 2px;
  }
  .signer { position: absolute; left: 64px; top: 633px; font-size: 11.3px; }

  .letter-footer {
    position: absolute; left: 0; right: 0; top: 748px; height: 52px;
    background: linear-gradient(90deg, var(--brand-deep) 0%, #4e63a8 45%, #c9d0e6 78%, #ffffff 100%);
    font-size: 6.6px; line-height: 8.6px; color: #fff;
  }
  .letter-footer .col { position: absolute; top: 6px; }
  .letter-footer .col-office { left: 77px; }
  .letter-footer .col-contact { left: 243px; width: 140px; text-align: right; }
  .letter-footer .col-bank { left: 410px; width: 120px; text-align: right; color: var(--brand-blue); }

  /* ---------- Business card ---------- */
  .business-card {
    position: absolute; left: 795px; top: 240px;
    width: 221px; height: 346px;
    background: var(--paper);
  }
  .business-card .brand { left: 20px; top: 30px; font-size: 17px; gap: 6px; }
  .business-card .brand-square { width: 10px; height: 10px; }
  .card-person {
    position: absolute; right: 12px; top: 128px; text-align: right; color: var(--brand-blue);
  }
  .card-person .degree { font-size: 14px; line-height: 18px; }
  .card-person .name { font-size: 18px; line-height: 22px; font-weight: 700; }
  .card-person .title { font-size: 9.5px; line-height: 13px; }
  .card-band {
    position: absolute; left: 0; right: 0; top: 262px; height: 62px;
    background: linear-gradient(90deg, var(--brand-deep) 0%, #4e63a8 50%, #c9d0e6 82%, #ffffff 100%);
    color: #fff; font-size: 7.4px; line-height: 9.6px; padding: 4px 0 0 21px;
  }
</style>
</head>
<body>

<section class="letterhead" aria-label="Briefpapier">
  <div class="brand"><span class="brand-square"></span>Lothar Venhaus</div>

  <div class="return-line">Lothar Venhaus • Steuerberater • Seeblickweg 12 B • 78299 Uferstadt</div>

  <address class="recipient" style="font-style:normal">
    Herrn<br>Max Mustermann<br>Musterstr. 1<br>12345 Musterstadt
  </address>

  <div class="references">
    <div>Ihr Zeichen:</div>
    <div>Ihre Nachricht vom:</div>
    <div>Unser Zeichen:</div>
    <div>Unsere Nachricht vom:</div>
    <div class="date">Datum:</div>
  </div>

  <span class="fold-mark" style="top:281px"></span>
  <span class="fold-mark" style="top:400px"></span>
  <span class="fold-mark" style="top:566px"></span>

  <div class="letter-body">
    <p>Sehr geehrter Herr Mustermann,</p>
    <p>Lorem ipsum dolor sit amet, consectetur adipisici elit, sed eiusmod tempor incidunt ut labore et dolore magna aliqua. Ut enim ad minim veniam, quis nostrud exercitation ullamco laboris nisi ut aliquid ex ea commodi consequat. Quis aute iure reprehenderit in voluptate velit esse cillum dolore eu fugiat nulla pariatur. Excepteur sint obcaecat cupiditat non proident, sunt in culpa qui officia deserunt mollit anim id est laborum.</p>
    <p>Duis autem vel eum iriure dolor in hendrerit in vulputate velit esse molestie consequat, vel illum dolore eu feugiat nulla facilisis at vero eros et accumsan et iusto odio dignissim qui blandit praesent luptatum zzril delenit augue duis dolore te feugait nulla facilisi. Lorem ipsum dolor sit amet, consectetuer adipiscing elit, sed diam nonummy nibh euismod tincidunt ut laoreet dolore magna aliquam erat volutpat.</p>
    <p>Ut wisi enim ad minim veniam, quis nostrud exerci tation ullamcorper suscipit lobortis nisl ut aliquip ex ea commodo consequat. Duis autem vel eum iriure dolor in hendrerit in vulputate velit esse molestie consequat, vel illum dolore eu feugiat nulla facilisis at vero eros et accumsan et iusto odio dignissim qui blandit praesent luptatum zzril delenit augue duis dolore te feugait nulla facilisi.</p>
    <p>Mit freundlichen Grüßen</p>
  </div>

  <div class="signature" role="img" aria-label="Handschriftliche Unterschrift"></div>
  <div class="signer">Lothar Venhaus</div>

  <footer class="letter-footer">
    <div class="col col-office">Lothar Venhaus<br>Steuerberater<br>Seeblickweg 12 B<br>78299 Uferstadt</div>
    <div class="col col-contact">Tel: +49 (0)7000-412390<br>Fax: +49 (0)7000-412391<br>E-Mail: info@venhaus-steuer.eu<br>St.Nr: 04518/27730</div>
    <div class="col col-bank">Bankname: XXXXX<br>BLZ: 12345678<br>Konto: 12345678<br>IBAN: DE12345678</div>
  </footer>
</section>

<section class="business-card" aria-label="Visitenkarte">
  <div class="brand"><span class="brand-square"></span>Lothar Venhaus</div>
  <div class="card-person">
    <div class="degree">Dipl.-Kaufmann</div>
    <div class="name">Lothar Venhaus</div>
    <div class="title">Steuerberater</div>
  </div>
  <div class="card-band">
    Seeblickweg 12 B<br>78299 Uferstadt<br>Tel: +49 (0)7000-412390<br>Fax: +49 (0)7000-412391<br>E-Mail: info@venhaus-steuer.eu
  </div>
</section>

</body>
</html>
```